New Business card design to reflect rebrand

I would like a business card design with a good base colour for our new logo and also a placeholder for a profile pic of the card holder. the design needs to be editable to the point that we can easily change the picture of the person and use that design for printmoor etc. we are looking at a metalic finish business card so will need a good base colour to bring out the finish.

Target Market(s)

prospective customers

Industry/Entity Type

Business

Contact Information for Business Card

I would like one editable design that we can change the name of the card holder and profile picture. The design need to be in a format that be send to printmoor etc.

Our address is Fenwick Lodge, Mill Lane, Ashcombe Green, RG41 3TQ Tel no. 01632 960417

Requirements
Must have
• place holder for a profile pic for the card holder. in AI or preferably PSD format

```html
<!DOCTYPE html>
<html lang="en">
<head>
<meta charset="utf-8">
<title>Corvane Workplace Services – Business Card</title>
<link rel="stylesheet" href="https://fonts.googleapis.com/css2?family=Montserrat:wght@400;500;600&family=Source+Sans+3:wght@700&display=swap">
<style>
  :root {
    --stage: #2c2d2c;
    --navy: #3e5470;
    --navy-deep: #3a4f69;
    --orange: #e05d22;
    --paper: #f7f7f6;
    --paper-shade: #e9e9e8;
    --ink: #1f1f1f;
    --white: #ffffff;
    --photo: #e6e6e6;
  }
  * { box-sizing: border-box; margin: 0; padding: 0; }
  html, body { width: 1200px; height: 1200px; overflow: hidden; background: var(--stage); }
  body { position: relative; font-family: "Montserrat", sans-serif; }

  .card { position: absolute; top: 442px; width: 512px; height: 300px; overflow: hidden; }
  .card--front { left: 81px; background: linear-gradient(200deg, var(--paper) 0%, var(--paper-shade) 100%); }
  .card--back { left: 607px; background: var(--navy); }

  .brand { position: absolute; left: 26px; top: 30px; display: flex; align-items: center; gap: 10px;
           font-family: "Montserrat", sans-serif; font-weight: 600; }
  .brand__mark { width: 14px; height: 14px; background: var(--orange); flex: none; }
  .brand__name { font-size: 30px; letter-spacing: 2px; line-height: 1.05; }
  .brand__name small { display: block; font-size: 12.5px; letter-spacing: 3.4px; margin-top: 6px; }
  .card--front .brand { color: var(--navy); }
  .card--back .brand { color: var(--white); left: 25px; }

  .holder { position: absolute; left: 26px; top: 161px; width: 389px; }
  .holder__name { font-family: "Source Sans 3", sans-serif; font-weight: 700; font-size: 16px;
                  color: var(--orange); letter-spacing: .5px; }
  .holder__title { display: flex; align-items: flex-end; font-size: 12.5px; color: var(--ink); margin-top: 3px; }
  .holder__title::after { content: ""; flex: 1; height: 1px; margin-left: 2px; margin-bottom: 3px;
                          background: linear-gradient(90deg, var(--orange), rgba(224,93,34,.1)); }

  .contacts { position: absolute; left: 26px; top: 216px; list-style: none; font-size: 12.5px; color: var(--ink); }
  .contacts li { display: flex; align-items: center; gap: 8px; height: 19px; }
  .contacts svg { width: 11px; height: 11px; flex: none; }

  .address { position: absolute; right: 25px; top: 236px; text-align: right; font-size: 12.5px;
             line-height: 18px; color: var(--ink); font-style: normal; }

  .footer-band { position: absolute; left: 0; bottom: 0; width: 100%; height: 20px; }

  .nameplate { position: absolute; left: 0; top: 195px; width: 100%; height: 57px; background: var(--orange);
               padding: 12px 0 0 28px; color: var(--white); font-family: "Source Sans 3", sans-serif; font-weight: 700; }
  .nameplate__name { font-size: 18px; letter-spacing: 1px; line-height: 1.1; }
  .nameplate__title { font-size: 11px; letter-spacing: .4px; }

  .profile-photo { position: absolute; left: 394px; top: 179px; width: 74px; height: 81px;
                   border: 1.5px solid var(--white); border-radius: 3px;
                   background: linear-gradient(180deg, #efefef, #d9d9d9); }
</style>
</head>
<body>

<section class="card card--front" aria-label="Business card front">
  <div class="brand">
    <span class="brand__mark"></span>
    <span class="brand__name">CORVANE<small>WORKPLACE SERVICES</small></span>
  </div>

  <div class="holder">
    <p class="holder__name">YOUR NAME</p>
    <p class="holder__title">Job Title</p>
  </div>

  <ul class="contacts">
    <li>
      <svg viewBox="0 0 11 11"><rect width="11" height="11" rx="1.5" fill="var(--orange)"/><path d="M2.5 4.5h6M3.5 4.5v3h4v-3" stroke="#fff" stroke-width="1.2" fill="none"/></svg>
      01632 960417
    </li>
    <li>
      <svg viewBox="0 0 11 11"><rect width="11" height="11" rx="1.5" fill="var(--orange)"/><rect x="2.3" y="3.3" width="6.4" height="4.4" fill="none" stroke="#fff" stroke-width="1"/><path d="M2.3 3.3l3.2 2.5 3.2-2.5" stroke="#fff" stroke-width="1" fill="none"/></svg>
      info@corvaneWS.com
    </li>
    <li>
      <svg viewBox="0 0 11 11"><rect width="11" height="11" rx="1.5" fill="var(--orange)"/><circle cx="5.5" cy="5.5" r="3" fill="none" stroke="#fff" stroke-width="1"/></svg>
      www.corvaneWS.com
    </li>
  </ul>

  <address class="address">Fenwick Lodge, Mill Lane<br>Ashcombe Green, RG41 3TQ</address>

  <svg class="footer-band" viewBox="0 0 512 20" preserveAspectRatio="none">
    <rect width="512" height="20" fill="var(--navy)"/>
    <polygon points="283,20 296,0 302,0 289,20" fill="var(--white)"/>
    <polygon points="289,20 302,0 512,0 512,20" fill="var(--orange)"/>
  </svg>
</section>

<section class="card card--back" aria-label="Business card back">
  <div class="brand">
    <span class="brand__mark"></span>
    <span class="brand__name">CORVANE<small>WORKPLACE SERVICES</small></span>
  </div>

  <div class="nameplate">
    <p class="nameplate__name">YOUR NAME</p>
    <p class="nameplate__title">JOB TITLE</p>
  </div>

  <div class="profile-photo" role="img" aria-label="Profile photo of the card holder"></div>
</section>

</body>
</html>
```